Voyage Wellcare Hub Business Cards

We need business cards for our new start-up online travel health clinic. Visit our website voyagewellcarehub.ca for branding and more info.

Target Market(s)

Travellers

Industry/Entity Type

Business

Contact Information for Business Card

Maya Koslowski
maya@voyagewellcarehub.ca
+1 555 283 6194
voyagewellcarehub.ca

Font styles to use
Sans Serif

Colors
f68d4d

```html
<!DOCTYPE html>
<html lang="en">
<head>
<meta charset="utf-8">
<title>Voyage Wellcare Hub – Business Cards</title>
<link rel="stylesheet" href="https://fonts.googleapis.com/css2?family=Montserrat:wght@400;600&display=swap">
<style>
  :root {
    --brand-orange: #f68d4d;
    --paper-white: #ffffff;
    --accent-grey: #b4b4b4;
    --tagline-grey: #9a9a9a;
    --stage: #e9e9e9;
  }
  * { margin: 0; padding: 0; box-sizing: border-box; }
  html, body { width: 1200px; height: 880px; overflow: hidden; }
  body {
    background: var(--stage);
    font-family: "Montserrat", Arial, sans-serif;
    display: flex;
    flex-direction: column;
    align-items: center;
    justify-content: center;
    gap: 40px;
  }
  .card {
    position: relative;
    width: 620px;
    height: 354px;
    overflow: hidden;
    box-shadow: 0 6px 18px rgba(0,0,0,.18);
  }

  /* Front */
  .card--front {
    background: var(--brand-orange);
    color: var(--paper-white);
    text-align: center;
  }
  .card--front .wordmark {
    position: absolute;
    top: 118px; left: 0; right: 0;
    font-size: 40px;
    font-weight: 400;
    letter-spacing: -0.5px;
  }
  .card--front .tagline {
    position: absolute;
    top: 172px; left: 0; right: 0;
    font-size: 15px;
    padding-left: 150px;
  }
  .card--front .website {
    position: absolute;
    top: 262px; left: 0; right: 0;
    font-size: 13px;
    letter-spacing: 5px;
  }

  /* Back */
  .card--back { background: var(--paper-white); }
  .card--back .sweep { position: absolute; inset: 0; }
  .card--back .wordmark {
    position: absolute;
    top: 88px; left: 40px;
    font-size: 36px;
    font-weight: 400;
    color: var(--brand-orange);
    letter-spacing: -0.5px;
  }
  .card--back .tagline {
    position: absolute;
    top: 136px; left: 170px;
    font-size: 14px;
    color: var(--tagline-grey);
  }
  .contact {
    position: absolute;
    right: 30px;
    top: 188px;
    color: var(--paper-white);
    text-align: right;
  }
  .contact__name {
    font-size: 17px;
    font-weight: 600;
    margin-bottom: 6px;
  }
  .contact__line {
    display: flex;
    justify-content: flex-end;
    align-items: center;
    gap: 8px;
    font-size: 12px;
    line-height: 22px;
  }
  .contact__icon { width: 16px; height: 16px; flex: none; }
</style>
</head>
<body>

  <section class="card card--front" aria-label="Business card front">
    <div class="wordmark">Voyage Wellcare Hub</div>
    <div class="tagline">Online Travel Health Experts</div>
    <div class="website">voyagewellcarehub.ca</div>
  </section>

  <section class="card card--back" aria-label="Business card back">
    <svg class="sweep" viewBox="0 0 620 354" preserveAspectRatio="none" aria-hidden="true">
      <path d="M525 0 C500 160 300 245 0 265 L0 354 L620 354 L620 0 Z" fill="var(--accent-grey)"/>
      <path d="M540 0 C520 170 330 270 0 300 L0 354 L620 354 L620 0 Z" fill="var(--brand-orange)"/>
      <path d="M540 0 C520 170 330 270 0 300" fill="none" stroke="var(--paper-white)" stroke-width="4"/>
    </svg>

    <div class="wordmark">Voyage Wellcare Hub</div>
    <div class="tagline">Online Travel Health Experts</div>

    <div class="contact">
      <div class="contact__name">Maya Koslowski</div>
      <div class="contact__line">+1 555 283 6194
        <svg class="contact__icon" viewBox="0 0 16 16" aria-hidden="true">
          <circle cx="8" cy="8" r="7" fill="none" stroke="#fff" stroke-width="1.2"/>
          <path d="M5.4 4.3l1.3-.3.7 1.8-.9.7c.4 1 1.1 1.7 2 2.1l.7-.9 1.8.7-.3 1.3c-3 .2-5.5-2.3-5.3-5.4z" fill="#fff"/>
        </svg>
      </div>
      <div class="contact__line">maya@voyagewellcarehub.ca
        <svg class="contact__icon" viewBox="0 0 16 16" aria-hidden="true">
          <circle cx="8" cy="8" r="7" fill="none" stroke="#fff" stroke-width="1.2"/>
          <rect x="4.2" y="5.3" width="7.6" height="5.4" fill="#fff"/>
          <path d="M4.2 5.3L8 8.4l3.8-3.1" fill="none" stroke="var(--brand-orange)" stroke-width=".9"/>
        </svg>
      </div>
      <div class="contact__line">voyagewellcarehub.ca
        <svg class="contact__icon" viewBox="0 0 16 16" aria-hidden="true">
          <circle cx="8" cy="8" r="7" fill="none" stroke="#fff" stroke-width="1.2"/>
          <circle cx="8" cy="8" r="4" fill="none" stroke="#fff" stroke-width=".9"/>
          <ellipse cx="8" cy="8" rx="1.7" ry="4" fill="none" stroke="#fff" stroke-width=".9"/>
          <path d="M4 8h8" stroke="#fff" stroke-width=".9"/>
        </svg>
      </div>
    </div>
  </section>

</body>
</html>
```